3D Printing Website redesign

We are in the process of redesigning our website. Attached is an image of one of the proposed pages - "The Brightlander". The idea with this page is that site visitors can get an indicative estimate of the cost of 3D Printing based on some provided metrics. When the user alters the metrics the price changes accordingly. We are looking for a design to support this page that will also be used across our site.

```html
<!DOCTYPE html>
<html lang="en">
<head>
<meta charset="utf-8">
<title>Layerform Studio – Pricing &amp; Quote</title>
<link rel="stylesheet" href="https://fonts.googleapis.com/css2?family=Questrial&display=swap">
<style>
  :root {
    --blue: #22a7ee;
    --blue-light: #8fd3fb;
    --ink: #222222;
    --page-top: #e8e8e8;
    --page-bottom: #d6d6d6;
    --white: #ffffff;
    --field: #e8e8e8;
    --field-edge: #c4c4c4;
    --rule: #9a9a9a;
    --footer: #282828;
    --thumb: #262626;
  }
  * { box-sizing: border-box; margin: 0; padding: 0; }
  html, body { width: 1200px; height: 1000px; overflow: hidden; }
  body {
    position: relative;
    font-family: "Questrial", "Century Gothic", sans-serif;
    color: var(--ink);
    background: var(--white);
  }
  .abs { position: absolute; }
  .hero {
    position: absolute; left: 0; top: 0; width: 1200px; height: 500px;
    background: linear-gradient(180deg, var(--page-top), var(--page-bottom));
  }
  .account-tab {
    left: 1018px; top: 20px; width: 142px; height: 30px;
    background: var(--white); border-radius: 8px 8px 0 0;
    color: var(--blue); font-size: 17px; text-align: center; line-height: 26px;
  }
  .account-tab .sep { margin: 0 6px; }
  .nav-bar {
    left: 41px; top: 47px; width: 1119px; height: 86px;
    background: var(--white); border-radius: 0 8px 8px 8px;
  }
  .brand {
    left: 14px; top: 22px; display: flex; align-items: center; gap: 10px;
    font-size: 24px; color: var(--blue); white-space: nowrap;
  }
  .brand-dot { width: 40px; height: 40px; border-radius: 50%; background: var(--blue); }
  .nav-item {
    top: 0; height: 86px; line-height: 82px; font-size: 17px;
    transform: translateX(-50%); white-space: nowrap;
  }
  .nav-item.is-active {
    transform: none; left: 469px; width: 164px; text-align: center;
    color: var(--white);
    background: linear-gradient(180deg, var(--blue-light), var(--blue));
  }
  .calculator { left: 41px; top: 190px; width: 1119px; height: 262px; }
  .calculator .rule { left: 0; width: 1119px; height: 2px; background: linear-gradient(90deg, var(--rule), rgba(154,154,154,0.3)); }
  .mode-tab {
    left: 0; width: 259px; height: 86px; background: var(--blue);
    color: var(--white); font-size: 17px; text-align: center; line-height: 86px;
    box-shadow: inset 0 -2px 3px rgba(0,0,0,0.12);
  }
  .metric-label { font-size: 17px; transform: translateX(-50%); white-space: nowrap; }
  .track { left: 430px; width: 259px; height: 5px; background: var(--blue); border-radius: 3px; }
  .thumb {
    width: 14px; height: 24px; border-radius: 7px; background: var(--thumb);
    border: 2px solid var(--white); transform: translate(-50%, -50%);
  }
  .result-shape {
    left: 926px; top: 87px; width: 130px; height: 130px; border-radius: 50%;
    background: radial-gradient(circle at 40% 35%, #e4f4fe, #9dd6f8 70%, var(--blue));
    opacity: 0.7;
  }
  .form-label { font-size: 17px; transform: translateX(-50%); white-space: nowrap; }
  .field {
    height: 30px; width: 259px; background: var(--field);
    border: 1px solid var(--field-edge); border-radius: 8px;
    box-shadow: inset 0 3px 4px rgba(0,0,0,0.25);
  }
  .field.is-textarea { height: 207px; }
  .captcha-code {
    color: var(--blue); font-size: 17px; letter-spacing: 5px; text-align: center; line-height: 28px;
    box-shadow: inset 0 1px 3px rgba(0,0,0,0.15);
  }
  .send-button {
    left: 902px; top: 737px; width: 259px; height: 30px; border-radius: 8px;
    background: var(--blue); color: var(--white); font-size: 17px; text-align: center; line-height: 30px;
  }
  .site-footer {
    left: 0; top: 925px; width: 1200px; height: 75px; background: var(--footer);
    color: var(--white); font-size: 12px;
  }
  .copyright { left: 41px; top: 23px; line-height: 15px; }
  .footer-links { right: 39px; top: 30px; white-space: nowrap; }
  .footer-links .sep { margin: 0 5px; }
</style>
</head>
<body>
  <div class="hero"></div>

  <div class="abs account-tab">Login<span class="sep">|</span>Register</div>

  <header class="abs nav-bar">
    <div class="abs brand"><span class="brand-dot"></span>Layerform Studio</div>
    <nav>
      <span class="abs nav-item" style="left:304px">SHOP</span>
      <span class="abs nav-item" style="left:404px">WHAT WE DO</span>
      <span class="abs nav-item is-active">PRICING &amp; QUOTE</span>
      <span class="abs nav-item" style="left:694px">PAGE NAME</span>
      <span class="abs nav-item" style="left:802px">GALLERY</span>
      <span class="abs nav-item" style="left:877px">DIY</span>
      <span class="abs nav-item" style="left:955px">TRAINING</span>
      <span class="abs nav-item" style="left:1057px">CONTACT</span>
    </nav>
  </header>

  <section class="abs calculator">
    <div class="abs rule" style="top:0"></div>
    <div class="abs mode-tab" style="top:2px">PRINT</div>
    <div class="abs mode-tab" style="top:88px">SCAN</div>
    <div class="abs mode-tab" style="top:174px">DESIGN</div>
    <div class="abs rule" style="top:260px"></div>

    <span class="abs metric-label" style="left:344px;top:34px">SQUARE</span>
    <div class="abs track" style="top:42px"></div>
    <div class="abs thumb" style="left:653px;top:44px"></div>
    <span class="abs metric-label" style="left:774px;top:34px">CIRCULAR</span>

    <span class="abs metric-label" style="left:344px;top:120px">SMALL</span>
    <div class="abs track" style="top:128px"></div>
    <div class="abs thumb" style="left:559px;top:130px"></div>
    <span class="abs metric-label" style="left:774px;top:120px">LARGE</span>

    <span class="abs metric-label" style="left:344px;top:206px">SPARSE</span>
    <div class="abs track" style="top:214px"></div>
    <div class="abs thumb" style="left:597px;top:216px"></div>
    <span class="abs metric-label" style="left:774px;top:206px">DENSE</span>

    <span class="abs metric-label" style="left:989px;top:34px">RESULT</span>
    <div class="abs result-shape" role="img" aria-label="Wireframe preview of the estimated printed shape"></div>
  </section>

  <form>
    <span class="abs form-label" style="left:170px;top:521px">NAME:*</span>
    <div class="abs field" style="left:41px;top:560px"></div>
    <span class="abs form-label" style="left:170px;top:609px">EMAIL:</span>
    <div class="abs field" style="left:41px;top:648px"></div>
    <span class="abs form-label" style="left:170px;top:698px">PHONE:*</span>
    <div class="abs field" style="left:41px;top:737px"></div>

    <span class="abs form-label" style="left:600px;top:521px">INSTRUCTIONS:</span>
    <div class="abs field is-textarea" style="left:471px;top:560px"></div>

    <span class="abs form-label" style="left:1031px;top:521px">CAPTCHA:</span>
    <div class="abs field captcha-code" style="left:902px;top:560px">YC9L4G</div>
    <div class="abs field" style="left:902px;top:648px"></div>
    <div class="abs send-button">SEND FORM</div>
  </form>

  <footer class="abs site-footer">
    <div class="abs copyright">© LAYERFORM STUDIO 2014<br>ALL RIGHTS RESERVED</div>
    <div class="abs footer-links">HOME<span class="sep">|</span>SHOP<span class="sep">|</span>WHAT WE DO<span class="sep">|</span>PRICING &amp; QUOTE<span class="sep">|</span>PAGE NAME<span class="sep">|</span>GALLERY<span class="sep">|</span>DIY<span class="sep">|</span>TRAINING<span class="sep">|</span>CONTACT</div>
  </footer>
</body>
</html>
```